-Photo booth rental Web Design Project

Our business is a small photo booth rental service serving the capital region and surrounding areas. The photo booth is a portable booth that fits up to 10 guest. I am looking for a website that will have social media capabilities and also private log ins for clients to view their photo albums online after their event. We provide full service photo booth rentals for all types of parties. I am looking for something fun and unique but also professional and I am also looking to maybe somehow incorporate the age of the photo booth which was invented in 1888. I do not have the photos of our photo booth available because we are just starting up and I wanted to get everything together first but I will provide stock photo booth pictures .Thank you for your patience i know it wont be an easy task with out those things. I added a word document describing information i will need on our website, i am looking for a home page, contact us and book an event page, online gallery page, and pricing. If you need any more information please feel free to contact me. Thanks for your help and I look forward to working with you.

Target Market(s)

For everyone from brides to be for their weddings or private parties, corporate parties, school dances, charity events, community events ect

Industry/Entity Type

Business

Requirements
Nice to have
• social media sharing

```html
<!DOCTYPE html>
<html lang="en">
<head>
<meta charset="utf-8">
<title>Giggle Frames Photo Booth</title>
<link href="https://fonts.googleapis.com/css2?family=Signika:wght@400;600&family=Arimo:wght@400;700&family=Alegreya:ital,wght@1,500&display=swap" rel="stylesheet">
<style>
:root{
  --brown-dark:#3b2518;
  --brown-mid:#7b4b33;
  --brown-light:#a0775a;
  --tan:#8c6b52;
  --card:#efefef;
  --card-line:#c9c9c9;
  --white:#ffffff;
  --ink:#333333;
  --grey:#666666;
}
*{box-sizing:border-box;margin:0;padding:0}
html,body{width:1200px;height:2343px;overflow:hidden;background:var(--white)}
body{position:relative;font-family:"Arimo",Arial,sans-serif;color:var(--ink)}
.abs{position:absolute}
.heading{font-family:"Signika",sans-serif}

/* header */
.brand{left:99px;top:4px;font-family:"Signika",sans-serif;font-weight:600;color:var(--brown-dark);font-size:38px;line-height:36px;display:flex;align-items:center;gap:12px}
.brand-dot{width:22px;height:22px;border-radius:50%;background:var(--brown-mid)}
.account-links{left:680px;top:54px;font-size:11px;color:var(--ink)}
.account-links span{margin:0 6px}
.search{left:857px;top:47px;width:244px;height:27px;border:1px solid #bbb;background:#fff;display:flex}
.search-field{flex:1;font-size:11px;color:#aaa;padding:7px 8px}
.search-btn{width:50px;background:#222;display:flex;align-items:center;justify-content:center}
.main-nav{left:99px;top:96px;width:1002px;height:46px;background:var(--brown-dark);border-radius:0 0 3px 3px}
.main-nav a{position:absolute;top:15px;color:#fff;font-size:14px;text-decoration:none}
.main-nav .current{left:43px;top:0;width:102px;height:35px;background:#fff;color:#222;text-align:center;padding-top:10px;border-radius:0 0 2px 2px}

/* hero */
.hero{left:0;top:142px;width:1200px;height:419px;background:linear-gradient(180deg,#ffffff 0%,#f2ede8 55%,#e8ddd3 100%)}
.hero-photo{left:185px;top:142px;width:830px;height:419px;background:linear-gradient(90deg,#d9c7b6,#efe6dc 30%,#e4d3c4 60%,#d6c0ae)}
.hero-arrow{top:302px;width:64px;height:64px;border-radius:50%;background:#e6e6e6;border:3px solid #fff;box-shadow:0 0 4px rgba(0,0,0,.2)}

/* about band */
.about{left:0;top:561px;width:1200px;height:416px;background:var(--brown-dark)}
.booth-photo{left:99px;top:610px;width:318px;height:302px;background:#fff;padding:6px}
.booth-photo div{width:100%;height:100%;background:linear-gradient(160deg,#2a1e1a,#7a2222 50%,#e9e4e0)}
.section-title{font-family:"Signika",sans-serif;color:var(--tan);font-size:25px;display:flex;align-items:center;gap:8px}
.section-title-rule{height:1px;background:#5c4232}
.body-copy{color:#fff;font-size:12.5px;line-height:19px}
.btn-brown{background:var(--brown-mid);color:#fff;font-size:12px;font-weight:700;border:1px solid #a07a63;text-align:center}
.mini-item-title{font-family:"Signika",sans-serif;color:var(--tan);font-size:17px}
.thumb{background:#fff;padding:3px}
.thumb div{width:100%;height:100%}

/* pricing */
.band-title{left:0;width:1200px;text-align:center;font-family:"Signika",sans-serif;font-weight:600;font-size:30px;display:flex;justify-content:center;align-items:center;gap:18px}
.band-title i{display:block;width:72px;height:6px;border-top:1px solid currentColor;border-bottom:1px solid currentColor}
.price-card{top:1098px;width:318px;height:292px;background:var(--card);border:1px solid var(--card-line);border-top:none}
.price-card-top{position:absolute;left:-1px;top:0;width:318px;height:28px;background:linear-gradient(180deg,#7b4b33,#4a2d1e);border-radius:3px 3px 0 0}
.price-name{position:absolute;left:24px;top:58px;font-family:"Signika",sans-serif;font-weight:600;font-size:30px;color:var(--ink)}
.price-tag{position:absolute;right:20px;top:13px;width:84px;height:84px;border-radius:50%;background:#fff;border:1px solid #ccc;font-family:"Alegreya",serif;font-style:italic;font-weight:500;font-size:30px;color:#222;text-align:center;line-height:82px}
.price-copy{position:absolute;left:26px;top:112px;width:270px;font-size:12px;line-height:19px;color:var(--grey)}
.btn-white{position:absolute;left:30px;bottom:-16px;width:106px;height:36px;background:#fff;border:1px solid #bbb;font-size:12px;font-weight:700;text-align:center;line-height:34px;color:#222}

/* featured */
.featured{left:0;top:1467px;width:1200px;height:461px;background:var(--brown-dark)}
.featured-box{left:209px;top:1565px;width:776px;height:294px;background:#fff;border-radius:4px;padding:6px}
.featured-inner{display:flex;height:100%;border:1px solid #999}
.featured-col{flex:1;background:var(--card);border-right:1px solid #bbb;padding:14px 16px;position:relative}
.featured-col:nth-child(even){background:#e6e6e6}
.featured-col:last-child{border-right:none}
.featured-col h3{font-family:"Signika",sans-serif;font-weight:400;font-size:17px;color:var(--ink)}
.featured-col p{font-size:11.5px;line-height:14px;color:var(--grey);margin-top:8px}
.featured-col .more{font-size:11.5px;color:#222;margin-top:10px}
.featured-col .thumb{position:absolute;left:30px;top:140px;width:138px;height:126px;border:1px solid #bbb}

/* lower */
.newsletter{left:99px;top:1982px;width:234px;height:258px;background:var(--brown-mid);border-radius:6px;padding:22px 34px}
.newsletter h3{font-family:"Signika",sans-serif;font-weight:400;font-size:21px;color:#fff;margin-bottom:28px}
.field{width:172px;height:32px;background:#fff;border:1px solid #ccc;font-size:11px;color:#555;padding:9px 8px;margin-bottom:13px}
.btn-send{width:106px;height:34px;background:#fff;font-size:12px;font-weight:700;color:#222;text-align:center;line-height:34px;margin-top:18px}
.col-title{font-family:"Signika",sans-serif;font-size:20px;color:var(--ink)}
.small-note{font-size:11.5px;color:var(--ink)}
.team-photo{top:2073px;width:120px;height:120px;border-radius:50%;border:4px solid #ddd;background:radial-gradient(circle at 50% 45%,#e8cbb6,#c7a78f 55%,#b8c4d2 56%,#d5dde6)}
.round-nav{top:2215px;width:36px;height:36px;border-radius:50%;border:3px solid var(--brown-mid);background:#fff}
.rule{height:1px;background:#aaa}
.call-box{left:783px;top:2159px;width:202px;height:84px}
.call-number{height:50px;background:var(--brown-dark);color:#fff;font-family:"Alegreya",serif;font-size:28px;text-align:center;line-height:50px;border-radius:3px 3px 0 0}
.call-label{height:34px;background:var(--brown-mid);color:#fff;font-size:14px;text-align:center;line-height:34px;border-top:2px solid #fff}

/* footer */
.site-footer{left:0;top:2288px;width:1200px;height:55px;background:var(--brown-dark);color:#fff;font-size:12px}
.footer-nav{position:absolute;left:99px;top:20px}
.footer-nav span{margin:0 6px}
.copyright{position:absolute;right:99px;top:20px}
</style>
</head>
<body>

<header>
  <div class="abs brand"><span class="brand-dot"></span><span>Giggle Frames<br>Photo Booth</span></div>
  <nav class="abs account-links">My Account<span>|</span>Login<span>|</span>Logout</nav>
  <div class="abs search">
    <div class="search-field">Search</div>
    <div class="search-btn"><svg width="22" height="22" viewBox="0 0 22 22"><circle cx="9" cy="9" r="6.5" fill="none" stroke="#fff" stroke-width="2.2"/><line x1="14" y1="14" x2="20" y2="20" stroke="#fff" stroke-width="2.6" stroke-linecap="round"/></svg></div>
  </div>
  <nav class="abs main-nav">
    <a class="current" href="#">Home</a>
    <a href="#" style="left:227px">About Us</a>
    <a href="#" style="left:383px">Pricing</a>
    <a href="#" style="left:530px">Our Gallery</a>
    <a href="#" style="left:702px">Events</a>
    <a href="#" style="left:846px">Contact Us</a>
  </nav>
</header>

<section>
  <div class="abs hero"></div>
  <div class="abs hero-photo" role="img" aria-label="Group of friends posing with moustache and glasses props"></div>
  <div class="abs hero-arrow" style="left:102px"><svg width="58" height="58" viewBox="0 0 58 58"><polyline points="34,17 22,29 34,41" fill="none" stroke="#999" stroke-width="5"/></svg></div>
  <div class="abs hero-arrow" style="left:1034px"><svg width="58" height="58" viewBox="0 0 58 58"><polyline points="24,17 36,29 24,41" fill="none" stroke="#999" stroke-width="5"/></svg></div>
</section>

<section class="abs about"></section>
<div class="abs booth-photo"><div role="img" aria-label="Couple standing beside a portable photo booth"></div></div>

<div class="abs" style="left:445px;top:604px;width:260px">
  <h2 class="section-title"><svg width="24" height="24" viewBox="0 0 24 24"><circle cx="12" cy="12" r="10.5" fill="none" stroke="#8c6b52" stroke-width="1.6"/><text x="12" y="17" text-anchor="middle" font-size="14" fill="#8c6b52" font-family="Arial">?</text></svg>Who We Are</h2>
  <div class="section-title-rule" style="margin-top:4px"></div>
</div>
<div class="abs body-copy" style="left:445px;top:647px;width:315px">
  <p>We are a family owned and operated photo booth rental company serving Maple, Cedar, Birch &amp; surrounding counties to create fun &amp; memorable memories for any type of event.</p>
  <p style="margin-top:19px">Our Booths feature the latest equipment and technology with SmartTouch screens, social and email uploading, MP3 player ready speaker systems, and dual "Photo Booth" or "Video Booth" modes with 1080p HD<br>Fun entertainment &amp; favors for all event types, ex: weddings, birthday parties, graduations, holiday parties, corporate parties, bar/ bat mitzvahs, bridal showers,</p>
</div>
<div class="abs btn-brown" style="left:442px;top:881px;width:105px;height:33px;line-height:31px">Read More</div>

<div class="abs" style="left:783px;top:604px;width:240px">
  <h2 class="section-title"><svg width="24" height="24" viewBox="0 0 24 24"><circle cx="12" cy="12" r="10.5" fill="none" stroke="#8c6b52" stroke-width="1.6"/><path d="M8 7c1-1 2 0 2.5 1.5s-1 1.5-.5 2.5 2 2.5 3 3 1.2-1 2.5-.5 1.5 1.5.5 2.5c-2 1.5-5-.5-7-3S6.5 8.5 8 7z" fill="#8c6b52"/></svg>Contact</h2>
  <div class="section-title-rule" style="margin-top:4px"></div>
</div>
<div class="abs heading" style="left:785px;top:648px;color:#fff;font-size:18px">24 Hours a Day, 7 Days a Week</div>
<div class="abs" style="left:785px;top:684px;color:#6e5240;font-size:12.5px;line-height:18px;width:280px">(555) 014-2290, 88 Shutter Lane, Brookvale<br>AB 12345</div>

<div class="abs thumb" style="left:783px;top:742px;width:79px;height:68px"><div role="img" aria-label="Wedding couple" style="background:linear-gradient(135deg,#d9c2b0,#8a6a5a)"></div></div>
<div class="abs mini-item-title" style="left:892px;top:736px">Wedding</div>
<div class="abs body-copy" style="left:892px;top:760px;width:200px;font-size:11.5px;line-height:15px">We provide full service photo booth rental for all types of parties.</div>
<div class="abs" style="left:892px;top:799px;color:#6e5240;font-size:11.5px">Read More →</div>

<div class="abs thumb" style="left:783px;top:845px;width:79px;height:70px;padding:0"><div role="img" aria-label="Party crowd under warm stage lights" style="background:linear-gradient(180deg,#f2b233,#c4521c 70%,#4a1f10)"></div></div>
<div class="abs mini-item-title" style="left:892px;top:840px">Parties</div>
<div class="abs body-copy" style="left:892px;top:866px;width:200px;font-size:11.5px;line-height:15px">We provide full service photo booth rental for all types of parties.</div>

<h2 class="abs band-title" style="top:1014px;color:var(--brown-dark)"><i></i>Pricing information<i></i></h2>

<article class="abs price-card" style="left:99px">
  <div class="price-card-top"></div>
  <h3 class="price-name">Standard</h3>
  <div class="price-tag">$675</div>
  <p class="price-copy">3 hours of service, set up &amp; removal, professional &amp; friendly booth attendant, dvd or usb flash drive of picture, guestbook, unlimited prints, online gallery, digital backdrop $675</p>
  <div class="btn-white">Read More</div>
</article>
<article class="abs price-card" style="left:442px">
  <div class="price-card-top"></div>
  <h3 class="price-name">Ultimate</h3>
  <div class="price-tag">$850</div>
  <p class="price-copy">4 hours of service, set up &amp; removal, professional &amp; friendly booth attendant, dvd or usb flash drive of picture gallery, guestbook, unlimited prints, custom backdrop, video messaging, props package, online gallery, instant social media uploads, digital back-drop $850</p>
  <div class="btn-white">Read More</div>
</article>
<article class="abs price-card" style="left:783px">
  <div class="price-card-top"></div>
  <h3 class="price-name">EXTREME</h3>
  <div class="price-tag">$975</div>
  <p class="price-copy">5 hours of service, set up &amp; removal, professional &amp; friendly booth attendant, dvd or usb flash drive of picture gallery, guestbook, unlimited prints, custom backdrop, video messaging, props pack-age, online gallery, red carpet event (velvet rope and carpet) , instant social media uploads, digital backdrop $975</p>
  <div class="btn-white">Read More</div>
</article>

<section class="abs featured"></section>
<h2 class="abs band-title" style="top:1494px;color:#fff"><i></i>Featured Listings<i></i></h2>
<div class="abs featured-box">
  <div class="featured-inner">
    <div class="featured-col"><h3>Wedding</h3><p>We provide full service photo booth rental for all types of parties.</p><div class="more">Read More →</div><div class="thumb"><div role="img" aria-label="Bride and groom" style="background:linear-gradient(135deg,#e6d3c2,#a77d68)"></div></div></div>
    <div class="featured-col"><h3>Parties</h3><p>We provide full service photo booth rental for all types of parties.</p><div class="more">Read More →</div><div class="thumb"><div role="img" aria-label="Party crowd with raised hands" style="background:linear-gradient(180deg,#f5c04a,#d2621f 65%,#5a2412)"></div></div></div>
    <div class="featured-col"><h3>Social</h3><p>We provide full service photo booth rental for all types of parties.</p><div class="more">Read More →</div><div class="thumb"><div role="img" aria-label="Friends taking a selfie" style="background:linear-gradient(135deg,#c84a3a,#e7b9a2 50%,#4a6a8a)"></div></div></div>
    <div class="featured-col"><h3>Charity</h3><p>We provide full service photo booth rental for all types of parties.</p><div class="more">Read More →</div><div class="thumb"><div role="img" aria-label="Hands holding a red heart" style="background:radial-gradient(circle,#d0202a 30%,#e8cdbd 70%)"></div></div></div>
  </div>
</div>

<section>
  <form class="abs newsletter">
    <h3>Newsletter</h3>
    <div class="field">Name</div>
    <div class="field">Email</div>
    <div class="btn-send">Send</div>
  </form>

  <h3 class="abs col-title" style="left:442px;top:1978px">Meet Our Team</h3>
  <div class="abs rule" style="left:628px;top:1992px;width:95px"></div>
  <p class="abs small-note" style="left:442px;top:2014px">Professional Photos of our team members</p>
  <div class="abs team-photo" style="left:443px" role="img" aria-label="Team member portrait"></div>
  <div class="abs team-photo" style="left:597px" role="img" aria-label="Team member portrait"></div>
  <div class="abs rule" style="left:442px;top:2233px;width:96px"></div>
  <div class="abs rule" style="left:636px;top:2233px;width:88px"></div>
  <div class="abs round-nav" style="left:543px"><svg width="30" height="30" viewBox="0 0 30 30"><polyline points="17,10 12,15 17,20" fill="none" stroke="#7b4b33" stroke-width="3"/></svg></div>
  <div class="abs round-nav" style="left:595px"><svg width="30" height="30" viewBox="0 0 30 30"><polyline points="13,10 18,15 13,20" fill="none" stroke="#7b4b33" stroke-width="3"/></svg></div>

  <h3 class="abs col-title" style="left:783px;top:1974px">Request a Time &amp; Cost Quote</h3>
  <p class="abs small-note" style="left:785px;top:2008px">Click Here to Fill-out Request Form</p>
  <div class="abs btn-brown" style="left:783px;top:2040px;width:106px;height:33px;line-height:31px">Click Here</div>
  <div class="abs rule" style="left:783px;top:2098px;width:302px"></div>
  <h3 class="abs col-title" style="left:783px;top:2114px">Request a Time &amp; Cost</h3>
  <div class="abs call-box">
    <div class="call-number">555-014-2290</div>
    <div class="call-label">Quote—Call Now!</div>
  </div>
</section>

<footer class="abs site-footer">
  <nav class="footer-nav">Home<span>|</span>About Us<span>|</span>Pricing<span>|</span>Our Gallery<span>|</span>Events<span>|</span>Contact Us</nav>
  <div class="copyright">Copyright © 2014. All Rights reserved.</div>
</footer>

</body>
</html>
```